Coffee Promotion for Specialty Coffees

I need to have a poster designed to promote our coffee sales. We offer cappuccino for $3.75, Latte for $3.75, Americano for $2.00, Espresso $2.00 and Fair Trade Organic Colombian Coffee for $1.75 Med, $2.00L Large. I would like sometihng very visual that shows the coffees and also has the pricing, and includes the wording" Try our Amazing Specialty Coffees!" Our logo is attached as well

Poster size is 24" wide x 36" high

Target Market(s)

Seniors and Students in a Mall Setting

Colors

Designer to choose colors to be used in the design.

Requirements
Must have
• Graphic artwork of coffees (cappuccinos, lattes, etc). Logo included in artwork. Must be for 24"wide x 36" high poster
Nice to have
• Would like something that shows closeups of the coffees and visually sells the coffee being premium and delicious.

```html
<!DOCTYPE html>
<html lang="en">
<head>
<meta charset="UTF-8">
<title>Specialty Coffees – Ember Bean</title>
<link href="https://fonts.googleapis.com/css2?family=Playball&family=Playfair+Display:ital,wght@0,400;0,700;1,700&display=swap" rel="stylesheet">
<style>
  :root {
    --night: #140a0e;
    --maroon: #4a0a14;
    --crimson: #8c0f1a;
    --deep-red: #5e0a12;
    --gold: #f2c55a;
    --gold-dark: #a9772a;
    --bar: #1d1416;
    --bar-top: #2a1f21;
    --bar-edge: #3a2a2c;
    --cream: #f6ecd8;
    --ring: #e9e2d6;
    --band: #2a1418;
    --coffee-light: #d8b48c;
    --coffee-mid: #9a6338;
    --coffee-dark: #4a2412;
    --teal: #2f8f8a;
  }
  * { box-sizing: border-box; margin: 0; padding: 0; }
  html, body { width: 829px; height: 1200px; overflow: hidden; }
  body {
    position: relative;
    background: linear-gradient(180deg, var(--night) 0%, var(--maroon) 28%, var(--crimson) 62%, var(--deep-red) 100%);
    font-family: "Playfair Display", Georgia, serif;
    color: var(--gold);
  }
  .starfield {
    position: absolute; inset: 0 0 auto 0; height: 520px;
    background:
      radial-gradient(ellipse at 15% 10%, rgba(190,110,60,.35), transparent 45%),
      radial-gradient(ellipse at 85% 18%, rgba(120,70,140,.35), transparent 45%),
      radial-gradient(ellipse at 50% 0%, rgba(160,90,50,.25), transparent 55%);
  }
  .brand {
    position: absolute; top: 72px; left: 0; right: 0;
    display: flex; justify-content: center; align-items: center; gap: 12px;
  }
  .brand-dot { width: 26px; height: 26px; border-radius: 50%; background: var(--cream); }
  .brand-name { font-size: 30px; font-weight: 700; color: var(--cream); line-height: 1; }
  .headline {
    position: absolute; top: 162px; left: 0; right: 0; text-align: center;
    font-family: "Playball", cursive; font-weight: 400;
    font-size: 84px; line-height: 1;
    color: var(--gold);
    text-shadow: 0 3px 6px rgba(0,0,0,.6);
  }
  .subhead {
    position: absolute; top: 266px; left: 0; right: 0; text-align: center;
    font-size: 32px; letter-spacing: 9px; color: var(--cream); line-height: 1;
  }
  .menu-bar {
    position: absolute; height: 66px;
    background: linear-gradient(180deg, var(--bar-top), var(--bar));
    border: 2px solid var(--bar-edge);
    border-radius: 6px;
    box-shadow: 0 6px 14px rgba(0,0,0,.55), inset 0 1px 0 rgba(255,255,255,.08);
    display: flex; align-items: center;
    font-style: italic; font-weight: 700; font-size: 34px;
    color: var(--gold);
    text-shadow: 0 2px 3px rgba(0,0,0,.7);
    white-space: nowrap;
  }
  .menu-bar.text-left { padding-left: 30px; }
  .menu-bar.text-right { padding-left: 60px; }
  .photo-slot {
    position: absolute; width: 156px; height: 156px; border-radius: 50%;
    border: 5px solid var(--ring);
    box-shadow: 0 8px 18px rgba(0,0,0,.6);
    background: linear-gradient(135deg, var(--coffee-light), var(--coffee-mid) 55%, var(--coffee-dark));
  }
  .photo-slot.dark { background: linear-gradient(135deg, var(--coffee-mid), var(--coffee-dark)); }
  .photo-slot.teal { width: 170px; height: 170px; background: linear-gradient(135deg, var(--teal), var(--coffee-mid)); }
  .fair-trade {
    flex-direction: column; align-items: stretch; justify-content: center;
    height: 96px; padding: 0 30px 0 100px;
    font-size: 27px; color: var(--cream);
  }
  .fair-trade .line { display: flex; justify-content: space-between; line-height: 1.3; }
  .base-band { position: absolute; left: 0; bottom: 0; width: 829px; height: 160px; }
  .closing {
    position: absolute; top: 1106px; left: 0; right: 0; text-align: center;
    font-style: italic; font-weight: 700; font-size: 38px; line-height: 1.2;
    color: var(--gold);
    text-shadow: 0 2px 4px rgba(0,0,0,.7);
  }
</style>
</head>
<body>
  <div class="starfield"></div>

  <header class="brand">
    <span class="brand-dot"></span>
    <span class="brand-name">Ember Bean</span>
  </header>

  <h1 class="headline">Specialty Coffees</h1>
  <p class="subhead">WE OFFER</p>

  <div class="menu-bar text-right" style="top:357px; left:200px; width:540px;">Cappuccino for $3.75</div>
  <div class="photo-slot" style="top:312px; left:100px;" role="img" aria-label="Photo: cappuccino with milk being poured"></div>

  <div class="menu-bar text-left" style="top:507px; left:90px; width:500px;">Latte for $3.75</div>
  <div class="photo-slot" style="top:462px; left:560px;" role="img" aria-label="Photo: latte with latte art on a saucer"></div>

  <div class="menu-bar text-right" style="top:657px; left:200px; width:540px;">Americano for $2.00</div>
  <div class="photo-slot dark" style="top:612px; left:100px;" role="img" aria-label="Photo: americano in a white cup"></div>

  <div class="menu-bar text-left" style="top:794px; left:90px; width:500px;">Espresso &nbsp;for $2.00</div>
  <div class="photo-slot dark" style="top:749px; left:560px;" role="img" aria-label="Photo: espresso with crema"></div>

  <div class="menu-bar fair-trade" style="top:935px; left:170px; width:570px;">
    <div class="line"><span>Fair Trade Organic</span><span>$1.75 (M)</span></div>
    <div class="line"><span>Colombian Coffee</span><span>$2.00 (L)</span></div>
  </div>
  <div class="photo-slot teal" style="top:898px; left:70px;" role="img" aria-label="Photo: Colombian coffee in a teal cup"></div>

  <svg class="base-band" viewBox="0 0 829 160" preserveAspectRatio="none" aria-hidden="true">
    <path d="M0 40 Q414 -20 829 40 L829 160 L0 160 Z" fill="var(--band)"/>
    <path d="M0 40 Q414 -20 829 40" fill="none" stroke="var(--gold-dark)" stroke-width="3"/>
  </svg>
  <p class="closing">Try Our Amazing Specialty Coffees!</p>
</body>
</html>
```